Grindstones- Tattoos/Piercings/Motorcycle/Biker Appearl Shop

Grindstones' buisness cards can be creative, playful and eye catching. Incorporate leather or diamond plate. We are an all female business. Biker theme, Tattoo Photos, Piercing Photos, Diamond plate, Leather and Girls!

This project needs to be an appointment card as well for the tattoo artists and piercers. We need a section that says APPT With: _______ , DATE, TIME, and then a QUOTE and DEPOSIT section for the artists. I attached the logo so you could incorportate that and have complete creative freedom. It's a biker store, we sell biker appearl and accessories, with a tattoo and piercing shop connected. Girls, Leather, Tattoos and Piercings. Have fun with it!
Updates

I've Updated project details for better description of what im looking for. Thanks!

Target Market(s)

Male and Female Ages 15-90. Interests in custom tattoos and quality piercings, bikers, motorcycle accessories like helmets, gloves, masks, leather, boots. Jewlery and clothes.

Industry/Entity Type

Business

Contact Information for Business Card

The business is called Grindstones, address, phone number and website. (2847 Larkmoor Rd. Harlow Bay, MI. 49517 (555)870-4152 www.inkvalleyshop.example)

Font styles to use
Serif
Sans Serif
Decorative
Script

Requirements
Must have
• Appointment with______
• Date_____ or MON TUES WED THUR etc... check mark boxes
• Time_____
• Quote______
• Deposit_______
• (231) 870-4152
• 2847 Larkmoor Rd
• Harlow Bay, MI 49517
• a facebook logo
Nice to have
• Owner Roy Pemberly
Should not have
• Tribal dragons or anything Tribal.That's cheesy! No Butterflies, No stars. No boys,

```html
<!DOCTYPE html>
<html lang="en">
<head>
<meta charset="utf-8">
<title>Grindstones – Business &amp; Appointment Card</title>
<link href="https://fonts.googleapis.com/css2?family=Exo+2:wght@300;400;500;600&display=swap" rel="stylesheet">
<style>
  :root {
    --page-bg: #d9d6d2;
    --card-dark: #141414;
    --card-mid: #2c2c2c;
    --seam: #3a3a3a;
    --seam-hi: #555;
    --ink: #f2f2f2;
    --ink-soft: #bdbdbd;
    --social: #2f7bd0;
  }
  * { box-sizing: border-box; margin: 0; padding: 0; }
  html, body { width: 1200px; height: 800px; overflow: hidden; background: var(--page-bg); }
  body { position: relative; font-family: "Exo 2", sans-serif; color: var(--ink); }

  .card {
    position: absolute;
    width: 580px;
    height: 331px;
    background: radial-gradient(ellipse at 55% 45%, var(--card-mid) 0%, var(--card-dark) 75%);
    box-shadow: 0 10px 28px rgba(0,0,0,.35);
    overflow: hidden;
  }
  .card-front { left: 560px; top: 50px; }
  .card-back  { left: 60px;  top: 410px; }

  .seam {
    position: absolute; left: 0; right: 0; height: 2px;
    background: var(--seam);
    border-bottom: 1px solid var(--seam-hi);
  }

  /* Front */
  .owner { position: absolute; left: 30px; top: 20px; }
  .owner-name { font-size: 17px; font-weight: 500; line-height: 1.2; }
  .owner-role { font-size: 12px; font-weight: 300; color: var(--ink-soft); }

  .brand-name {
    position: absolute;
    font-weight: 500;
    color: var(--ink);
    letter-spacing: 1px;
    white-space: nowrap;
  }
  .card-front .brand-name { left: 0; right: 0; text-align: center; top: 98px; font-size: 66px; line-height: 1.1; }
  .card-back  .brand-name { right: 40px; bottom: 24px; font-size: 38px; line-height: 1.1; }

  .contact {
    position: absolute; left: 100px; top: 210px; width: 380px;
    font-size: 15px; line-height: 1.45; text-align: center;
  }
  .social-square {
    position: absolute; right: 28px; bottom: 22px;
    width: 34px; height: 34px; background: var(--social);
  }

  /* Back */
  .appt-form { position: absolute; left: 34px; top: 24px; right: 34px; font-size: 15px; }
  .form-row { display: flex; align-items: flex-end; margin-bottom: 10px; }
  .form-label { white-space: nowrap; }
  .form-label.fixed { width: 80px; }
  .fill-line { flex: 1; border-bottom: 2px dotted var(--ink); margin-left: 8px; height: 14px; }
  .days { display: flex; justify-content: space-between; margin: 2px 0 12px; font-size: 14px; }
  .day { display: flex; align-items: center; gap: 5px; white-space: nowrap; }
  .check-box { width: 16px; height: 16px; background: var(--ink); }
</style>
</head>
<body>

  <section class="card card-front" aria-label="Business card front">
    <div class="seam" style="top:62px"></div>
    <div class="seam" style="top:200px"></div>
    <div class="owner">
      <div class="owner-name">Roy Pemberly</div>
      <div class="owner-role">Owner</div>
    </div>
    <div class="brand-name">Grindstones</div>
    <div class="contact">
      <div>(555)870-4152</div>
      <div>www.inkvalleyshop.example</div>
      <div>2847 Larkmoor Rd. Harlow Bay, MI. 49517</div>
    </div>
    <div class="social-square" aria-label="Social page"></div>
  </section>

  <section class="card card-back" aria-label="Appointment card back">
    <div class="seam" style="top:14px"></div>
    <div class="seam" style="top:236px"></div>
    <div class="appt-form">
      <div class="form-row">
        <span class="form-label">Appointment With:</span><span class="fill-line"></span>
      </div>
      <div class="days">
        <span class="day"><span class="check-box"></span>Mon</span>
        <span class="day"><span class="check-box"></span>Tue</span>
        <span class="day"><span class="check-box"></span>Wed</span>
        <span class="day"><span class="check-box"></span>Thu</span>
        <span class="day"><span class="check-box"></span>Fri</span>
        <span class="day"><span class="check-box"></span>Sat</span>
        <span class="day"><span class="check-box"></span>Sun</span>
      </div>
      <div class="form-row"><span class="form-label fixed">Time :</span><span class="fill-line"></span></div>
      <div class="form-row"><span class="form-label fixed">Quote :</span><span class="fill-line"></span></div>
      <div class="form-row"><span class="form-label fixed">Deposit :</span><span class="fill-line"></span></div>
    </div>
    <div class="brand-name">Grindstones</div>
  </section>

</body>
</html>
```